Women's Online Clothing Boutique Needs Business Cards

I already have a logo that I would like to use. Some of the things that interest me is black business cards, foil embossed logo, glossy embossed logo, leopard print, no yellow font, rounded edges. I even like just a large logo on the front side with all of my information on the back side.

Contact Information for Business Card

https://silverheron.shopvenlo.com/
https://www.pagelink.net/thesilverheronboutique/
https://www.picfeed.net/thesilverheronboutique/
silverheronboutique@mailora.net

Requirements
Must have
• My Logo
Nice to have
• Leopard Print
Should not have
• No Yellow Font

```html
<!DOCTYPE html>
<html lang="en">
<head>
<meta charset="utf-8">
<title>The Silver Heron Boutique – Business Cards</title>
<link rel="stylesheet" href="https://fonts.googleapis.com/css2?family=Josefin+Sans:wght@400&family=Roboto+Condensed:wght@400&display=swap">
<style>
  :root {
    --backdrop: #1c1c1c;
    --card: #0a0a0a;
    --card-sheen: #1e1e1e;
    --gold: #c9a24a;
    --ink: #f2f2f2;
  }
  * { box-sizing: border-box; margin: 0; padding: 0; }
  html, body { width: 1200px; height: 930px; overflow: hidden; }
  body {
    background: var(--backdrop);
    position: relative;
    font-family: "Roboto Condensed", sans-serif;
  }
  .card {
    position: absolute;
    width: 540px;
    height: 310px;
    border-radius: 22px;
    background: linear-gradient(125deg, var(--card) 0%, var(--card-sheen) 45%, var(--card) 70%);
    box-shadow: 0 18px 40px rgba(0,0,0,0.55);
    overflow: hidden;
  }
  .card--front { left: 80px; top: 90px; }
  .card--back { left: 580px; top: 500px; }

  .brand {
    position: absolute;
    left: 0; right: 0;
    display: flex;
    align-items: center;
    justify-content: center;
    gap: 12px;
    font-family: "Josefin Sans", sans-serif;
    font-weight: 400;
    color: var(--gold);
    letter-spacing: 0.5px;
    white-space: nowrap;
  }
  .brand__dot {
    width: 12px; height: 12px;
    border-radius: 50%;
    background: var(--gold);
  }
  .card--front .brand { top: 135px; font-size: 34px; }
  .card--back .brand { top: 62px; font-size: 28px; }

  .divider {
    position: absolute;
    left: 36px; right: 36px;
    top: 168px;
    height: 1px;
    background: var(--gold);
  }
  .contacts {
    position: absolute;
    top: 190px;
    left: 36px; right: 36px;
    display: flex;
    justify-content: space-between;
    font-size: 15px;
    color: var(--ink);
  }
  .contacts__group { list-style: none; display: flex; flex-direction: column; gap: 8px; }
  .contacts__group--right { align-items: flex-end; }
  .contacts__item { display: flex; align-items: center; gap: 8px; }
  .contacts__icon {
    width: 16px; height: 16px;
    border-radius: 50%;
    background: var(--gold);
    flex: none;
  }
</style>
</head>
<body>
  <section class="card card--front" aria-label="Card front">
    <div class="brand"><span class="brand__dot"></span>The Silver Heron Boutique</div>
  </section>

  <section class="card card--back" aria-label="Card back">
    <div class="brand"><span class="brand__dot"></span>The Silver Heron Boutique</div>
    <div class="divider"></div>
    <div class="contacts">
      <ul class="contacts__group">
        <li class="contacts__item"><span class="contacts__icon"></span>thesilverheronboutique/</li>
        <li class="contacts__item"><span class="contacts__icon"></span>thesilverheronboutique/</li>
      </ul>
      <ul class="contacts__group contacts__group--right">
        <li class="contacts__item">silverheronboutique@mailora.net<span class="contacts__icon"></span></li>
        <li class="contacts__item">silverheron.shopvenlo.com<span class="contacts__icon"></span></li>
      </ul>
    </div>
  </section>
</body>
</html>
```